Lumo4Kart - a fintech company - business card

We need a business card design for our Payments Technology company in Sydney, Australia. We provide business with payment solutions expanding across EFTPOS machines, online payment gateways and mobile payment solutions. We would like to see designs that are clean, classy and professional.
Target Market(s)
Business professionals, executives, c-suite
Industry/Entity Type
Fintech
Contact Information for Business Card
Will be on 400gsm. Logo will most likely be spot gloss unless designer recommends otherwise.
Font styles to use
Sans Serif
Requirements
Must have
- We need our website (lumo4kart.com.au), email (contact@lumo4kart.com.au), mobile (0432 587 904) and direct phone number (02 6815 3927) to feature on the card along with our logo (attached) and the words "EFTPOS | ONLINE | MOBILE"
- Font = Roboto

```html
<!DOCTYPE html>
<html lang="en">
<head>
<meta charset="utf-8">
<title>Lumo4Kart – Business Card</title>
<link rel="stylesheet" href="https://fonts.googleapis.com/css2?family=Roboto:wght@400&family=Roboto+Condensed:wght@300;400&display=swap">
<style>
  :root {
    --brand-green: #1e7b3c;
    --paper: #ffffff;
  }
  * { margin: 0; padding: 0; box-sizing: border-box; }
  html, body {
    width: 1200px;
    height: 1200px;
    overflow: hidden;
    background: var(--paper);
  }
  .card {
    position: relative;
    width: 1200px;
    height: 1200px;
    background: var(--paper);
    color: var(--brand-green);
    font-family: "Roboto", sans-serif;
  }
  .brand-mark {
    position: absolute;
    left: 84px;
    top: 150px;
    width: 140px;
    height: 140px;
    background: var(--brand-green);
  }
  .brand-name {
    position: absolute;
    left: 243px;
    top: 145px;
    width: 440px;
    font-family: "Roboto Condensed", sans-serif;
    font-weight: 300;
    font-size: 90px;
    line-height: 1;
    white-space: nowrap;
    overflow: hidden;
  }
  .tagline {
    position: absolute;
    left: 247px;
    top: 257px;
    font-family: "Roboto Condensed", sans-serif;
    font-weight: 400;
    font-size: 38px;
    line-height: 1;
    white-space: nowrap;
  }
  .divider {
    position: absolute;
    left: 702px;
    top: 143px;
    width: 1px;
    height: 182px;
    background: var(--brand-green);
  }
  .contact-list {
    position: absolute;
    left: 732px;
    top: 146px;
    width: 440px;
    list-style: none;
    font-family: "Roboto Condensed", sans-serif;
    font-weight: 400;
    font-size: 31px;
    line-height: 44px;
    letter-spacing: -0.8px;
    white-space: nowrap;
  }
  .contact-label { margin-right: 5px; }
  .person-name {
    position: absolute;
    left: 718px;
    top: 550px;
    font-family: "Roboto", sans-serif;
    font-weight: 400;
    font-size: 96px;
    line-height: 1;
    letter-spacing: -2px;
    white-space: nowrap;
  }
</style>
</head>
<body>
  <main class="card">
    <div class="brand-mark" aria-hidden="true"></div>
    <div class="brand-name">LUMO4KART</div>
    <div class="tagline">EFTPOS | ONLINE | MOBILE</div>

    <div class="divider" aria-hidden="true"></div>

    <ul class="contact-list">
      <li><span class="contact-label">website:</span>http://lumo4kart.com.au</li>
      <li><span class="contact-label">email:</span>contact@lumo4kart.com.au</li>
      <li><span class="contact-label">mobile phone:</span>0432 587 904</li>
      <li><span class="contact-label">direct&nbsp;&nbsp; phone:</span>02 6815 3927</li>
    </ul>

    <div class="person-name">John Doe</div>
  </main>
</body>
</html>
```